NestPath Realty needs a business card design.

Please view my website at www.nestpathrealty.example to learn about my business and my marketing style. I need a business template...one where I can change the names for all my employees. I'm hoping two find 2 designs that I like so my agents have a choice.

We're a real estate company. Instead of the standard self portraits that other Realtors use, we use monkeys. I need it two sided.... need to have our logo, monkey pic, agents name & info. Don't need room for a physical address, just name, title, phone number, email, website address.

Need the tagline: Don't Let Them Make a Monkey Out of You!

Corinne Talbeck ABR, GRI
Exclusive Buyer Broker
NestPath Realty

214-555-0198
Corinne@NestPathRealty.example
www.NestPathRealty.example

Attached our logo and a couple of monkey pics. It's okay to crop the monkey, but the monkey needs to be a dominate part of the card. I actually almost prefer a head shot of the monkey but I'm open. I've also attached some designs that I like.
Updates

MUST have the tagline: Don't Let Them Make a Monkey Out of You!

Industry/Entity Type

Real Estate

Requirements
Must have
• Must have my tagline below on the card:

Don't Let Them Make a Monkey Out of You!

Use 2 different monkey pics attached.
Nice to have
• I'd like to change the bow lipstick color on the monkey to red.

```html
<!DOCTYPE html>
<html lang="en">
<head>
<meta charset="utf-8">
<title>NestPath Realty — Business Card</title>
<link href="https://fonts.googleapis.com/css2?family=Great+Vibes&family=Tinos&family=Open+Sans:wght@400;600&display=swap" rel="stylesheet">
<style>
  :root {
    --stage: #2a2a2a;
    --card: #ffffff;
    --navy: #0f1a5c;
    --crimson: #9b0a14;
    --ink-light: #ffffff;
    --tagline: #f4d6d8;
    --logo-navy: #1c2a6e;
    --fur-dark: #2b1d16;
    --fur-mid: #5a3e30;
  }
  * { box-sizing: border-box; margin: 0; padding: 0; }
  html, body { width: 1200px; height: 900px; overflow: hidden; }
  body {
    background: var(--stage);
    display: flex;
    align-items: center;
    justify-content: center;
    gap: 90px;
  }
  .card {
    position: relative;
    width: 340px;
    height: 595px;
    background: var(--card);
    border-radius: 14px;
    overflow: hidden;
  }

  /* Back side */
  .card-back .mascot-standing {
    position: absolute;
    left: 50px; top: 40px;
    width: 240px; height: 400px;
    border-radius: 40px;
    background: radial-gradient(ellipse at 50% 40%, var(--fur-mid), var(--fur-dark) 75%);
  }
  .brand {
    position: absolute;
    left: 0; right: 0; bottom: 58px;
    display: flex;
    align-items: center;
    justify-content: center;
    gap: 10px;
    font-family: "Tinos", serif;
    font-size: 34px;
    color: var(--logo-navy);
  }
  .brand-mark {
    width: 16px; height: 16px;
    border-radius: 50%;
    background: var(--crimson);
  }

  /* Front side */
  .card-front .shape-layer { position: absolute; inset: 0; }
  .tagline {
    position: absolute;
    top: 26px; left: 40px; right: 40px;
    text-align: center;
    font-family: "Open Sans", sans-serif;
    font-size: 17px;
    line-height: 1.3;
    color: var(--tagline);
  }
  .card-front .mascot-sitting {
    position: absolute;
    left: 95px; top: 145px;
    width: 150px; height: 200px;
    border-radius: 36px;
    background: radial-gradient(ellipse at 50% 40%, var(--fur-mid), var(--fur-dark) 75%);
  }
  .agent {
    position: absolute;
    left: 34px; right: 20px; bottom: 34px;
    color: var(--ink-light);
    font-family: "Tinos", serif;
  }
  .agent-name {
    font-family: "Great Vibes", cursive;
    font-size: 40px;
    font-weight: 400;
    line-height: 1.1;
  }
  .agent-title { font-size: 17px; margin-top: 6px; }
  .agent-contact { list-style: none; margin-top: 26px; font-size: 15px; line-height: 1.45; }
</style>
</head>
<body>

  <section class="card card-back" aria-label="Card back">
    <div class="mascot-standing" role="img" aria-label="Cartoon monkey with a pink bow, standing and smiling"></div>
    <div class="brand">
      <span class="brand-mark"></span>
      <span class="brand-name">NestPath Realty</span>
    </div>
  </section>

  <section class="card card-front" aria-label="Card front">
    <svg class="shape-layer" width="340" height="595" viewBox="0 0 340 595" aria-hidden="true">
      <path d="M0 0 H340 V70 Q170 150 0 70 Z" fill="var(--crimson)"/>
      <path d="M0 360 Q170 305 340 360 V595 H0 Z" fill="var(--navy)"/>
    </svg>
    <p class="tagline">Don't Let Them Make a Monkey<br>Out of You!</p>
    <div class="mascot-sitting" role="img" aria-label="Cartoon monkey with a pink bow, sitting with hands clasped"></div>
    <div class="agent">
      <h1 class="agent-name">Corinne Talbeck</h1>
      <p class="agent-title">Exclusive Buyer Broker</p>
      <ul class="agent-contact">
        <li>214-555-0198</li>
        <li>Corinne@NestPathRealty.example</li>
        <li>www.NestPathRealty.example</li>
      </ul>
    </div>
  </section>

</body>
</html>
```